Plover Freightworks Business Card Design

We are a trucking and warehousing company. We run freight in the US manly from the Pacific NW to TX and back up the the PNW. We also do warehousing where we store, move, and distribute freight. Looking for a clean and modern design of business card. We would like to look rich and elegant. Attached is our logo.

Industry/Entity Type

Trucking Company

Contact Information for Business Card

Looking for a clean and modern design of business card. We would like to look rich and elegant.

Font styles to use
Sans Serif

Colors

Designer to choose colors to be used in the design.

Requirements
Must have
• logo but it should not dominate the card
Should not have
• logo should not dominate the card

```html
<!DOCTYPE html>
<html lang="en">
<head>
<meta charset="utf-8">
<title>Plover Freightworks Business Card</title>
<link href="https://fonts.googleapis.com/css2?family=Jost:ital,wght@0,400;0,500;0,700;1,700&display=swap" rel="stylesheet">
<style>
  :root {
    --backdrop: #4a3123;
    --card: #333333;
    --ink: #232323;
    --ink-soft: #262626;
  }
  html, body {
    margin: 0;
    padding: 0;
    width: 1200px;
    height: 1200px;
    overflow: hidden;
    background: var(--backdrop);
    font-family: "Jost", sans-serif;
  }
  .canvas {
    position: relative;
    width: 1200px;
    height: 1200px;
  }
  .card {
    position: absolute;
    background: var(--card);
    border-radius: 40px;
    color: var(--ink);
  }
  .card-front {
    left: 221px;
    top: 132px;
    width: 749px;
    height: 428px;
  }
  .card-back {
    left: 218px;
    top: 630px;
    width: 763px;
    height: 438px;
  }
  .wordmark {
    position: absolute;
    display: flex;
    align-items: center;
    gap: 12px;
    font-weight: 500;
    letter-spacing: 0.04em;
    text-transform: uppercase;
    color: var(--ink);
    white-space: nowrap;
  }
  .wordmark-dot {
    border-radius: 50%;
    background: var(--ink);
    flex: none;
  }
  .card-front .wordmark {
    left: 50%;
    top: 190px;
    transform: translateX(-50%);
    font-size: 30px;
  }
  .card-front .wordmark-dot {
    width: 40px;
    height: 40px;
  }
  .card-back .wordmark {
    right: 62px;
    top: 112px;
    font-size: 15px;
  }
  .person-name {
    position: absolute;
    left: 57px;
    top: 112px;
    margin: 0;
    font-size: 47px;
    font-weight: 700;
    line-height: 1;
    letter-spacing: 0.01em;
    color: var(--ink);
  }
  .person-title {
    position: absolute;
    left: 63px;
    top: 158px;
    margin: 0;
    font-size: 19px;
    font-weight: 700;
    color: var(--ink);
  }
  .contact {
    position: absolute;
    left: 63px;
    top: 262px;
    display: grid;
    grid-template-columns: 87px auto;
    row-gap: 6px;
    font-size: 17px;
    line-height: 1.3;
    margin: 0;
  }
  .contact dt {
    font-weight: 700;
    font-style: italic;
    color: var(--ink);
  }
  .contact dd {
    margin: 0;
    font-weight: 400;
    color: var(--ink-soft);
  }
</style>
</head>
<body>
<main class="canvas">
  <section class="card card-front" aria-label="Card front">
    <div class="wordmark"><span class="wordmark-dot"></span>Plover Freightworks, LLC</div>
  </section>

  <section class="card card-back" aria-label="Card back">
    <h1 class="person-name">YOUR NAME</h1>
    <p class="person-title">job title</p>
    <div class="wordmark">Plover Freightworks, LLC</div>
    <dl class="contact">
      <dt>address.</dt>
      <dd>123 Lorem Ipsum,<br>Lorem, City 12345</dd>
      <dt>email.</dt>
      <dd>youremail@yourdomain.com</dd>
      <dt>phone.</dt>
      <dd>123.456.7891</dd>
    </dl>
  </section>
</main>
</body>
</html>
```